Business card for a young woman who performs life enhancement activities with people who have developmental disabilities, what used to be called retardation. She wants to focus on the creative part of her work. She has a degree in art and will engage clients in art projects as well as helping them learn to do things like grocery shop, cook meals, set goals, and live independently.

Target Market(s)

Parents, caregivers, guardians, relatives of people with developmental disabilities, meaning they have not developed in their mental capacities.

Industry/Entity Type

Business

Contact Information for Business Card

Bright Harbor Services, Marisa T. Dunlop, 417 362-8094, marisa@marisadunlop.example, Life enhancement services for people with developmental disabilities. No address.

Font styles to use
Serif

Requirements
Must have
• Marisa wants it to have some indication of the art or creative part of her work with clients. But it must also be businesslike so it appeals to the parents. They have to see her as a professional, but she's compassionate and artsy. She wants just her company name on the front. The other information should be on the back.

```html
<!DOCTYPE html>
<html lang="en">
<head>
<meta charset="utf-8">
<title>Bright Harbor Services – Business Card</title>
<link rel="stylesheet" href="https://fonts.googleapis.com/css2?family=Lora:wght@400&display=swap">
<style>
  :root {
    --backdrop: #e9e6e1;
    --card: #ffffff;
    --ink: #3a3d8c;
    --ink-soft: #4a4f9e;
    --photo-top: #c9c2b4;
    --photo-bottom: #8a6f64;
    --shadow: rgba(40, 30, 20, 0.22);
    --paint-red: #d8453b;
    --paint-orange: #ee9a2e;
    --paint-yellow: #e9cf3a;
    --paint-green: #4fae5a;
    --paint-blue: #3a7cc4;
    --paint-violet: #7b4fa8;
  }
  * { box-sizing: border-box; margin: 0; padding: 0; }
  html, body {
    width: 1200px;
    height: 914px;
    overflow: hidden;
    background: var(--backdrop);
    font-family: "Lora", Georgia, serif;
    color: var(--ink);
  }
  .canvas {
    position: relative;
    width: 1200px;
    height: 914px;
  }
  .card {
    position: absolute;
    left: 240px;
    width: 720px;
    height: 411px;
    background: var(--card);
    box-shadow: 0 6px 18px var(--shadow);
    overflow: hidden;
  }
  .card--brand { top: 30px; }
  .card--contact { top: 473px; }

  .paint-band {
    position: absolute;
    left: 0;
    right: 0;
    bottom: 0;
    height: 10px;
    background: linear-gradient(90deg,
      var(--paint-red) 0 16.66%,
      var(--paint-orange) 16.66% 33.33%,
      var(--paint-yellow) 33.33% 50%,
      var(--paint-green) 50% 66.66%,
      var(--paint-blue) 66.66% 83.33%,
      var(--paint-violet) 83.33% 100%);
  }

  .brand {
    position: absolute;
    display: flex;
    align-items: center;
    gap: 12px;
  }
  .brand__mark {
    width: 16px;
    height: 16px;
    border-radius: 50%;
    background: var(--ink);
    flex: none;
  }
  .brand__name {
    font-size: 40px;
    line-height: 1;
    color: var(--ink);
    white-space: nowrap;
  }
  .card--brand .brand {
    right: 52px;
    top: 250px;
  }
  .tagline {
    position: absolute;
    right: 52px;
    top: 316px;
    font-size: 18px;
    font-style: italic;
    color: var(--ink-soft);
    white-space: nowrap;
  }

  .photo {
    position: absolute;
    left: 30px;
    top: 30px;
    width: 345px;
    height: 320px;
    background: linear-gradient(170deg, var(--photo-top), var(--photo-bottom));
  }
  .details {
    position: absolute;
    left: 390px;
    top: 70px;
    width: 315px;
    text-align: center;
  }
  .details .brand {
    position: static;
    justify-content: center;
    gap: 10px;
    margin-bottom: 26px;
  }
  .details .brand__name { font-size: 24px; }
  .details .brand__mark { width: 11px; height: 11px; }
  .person {
    font-size: 28px;
    line-height: 1.2;
    color: var(--ink);
    margin-bottom: 26px;
  }
  .contact-line {
    font-size: 18px;
    color: var(--ink-soft);
    line-height: 1.7;
    white-space: nowrap;
  }
</style>
</head>
<body>
<main class="canvas">
  <section class="card card--brand">
    <div class="brand">
      <span class="brand__mark"></span>
      <span class="brand__name">Bright Harbor Services</span>
    </div>
    <p class="tagline">Life enhancement services for people with developmental disabilities</p>
    <div class="paint-band"></div>
  </section>

  <section class="card card--contact">
    <div class="photo" role="img" aria-label="Photo of Marisa smiling cheek to cheek with a client"></div>
    <div class="details">
      <div class="brand">
        <span class="brand__mark"></span>
        <span class="brand__name">Bright Harbor Services</span>
      </div>
      <p class="person">Marisa T. Dunlop</p>
      <p class="contact-line">417 362-8094</p>
      <p class="contact-line">marisa@marisadunlop.example</p>
    </div>
    <div class="paint-band"></div>
  </section>
</main>
</body>
</html>
```